Quarlwick Builders Business Cards

I want to use the logo and make an unique business card that shows the textured Logo with brick and builings. I want to be able to stand out when I pass out business cards.

```html
<!DOCTYPE html>
<html lang="en">
<head>
<meta charset="utf-8">
<title>Quarlwick Builders Business Cards</title>
<link rel="stylesheet" href="https://fonts.googleapis.com/css2?family=Arimo:wght@400;700&family=Oswald:wght@400&display=swap">
<style>
  :root {
    --backdrop: #5a5a5a;
    --card-white: #ffffff;
    --brick: #d9442a;
    --brick-deep: #a8321f;
    --brick-glow: #c7401f;
    --ink: #4a4a4a;
    --ink-dark: #2a2320;
    --rule: #c9c9c9;
    --steel-dark: #5d5d5a;
    --steel-light: #9a9a92;
  }
  html, body {
    margin: 0;
    width: 1200px;
    height: 1200px;
    overflow: hidden;
    background: var(--backdrop);
  }
  .sheet {
    position: relative;
    width: 1200px;
    height: 1200px;
  }
  .card {
    position: absolute;
    left: 262px;
    width: 690px;
    height: 393px;
    overflow: hidden;
  }
  .card-front { top: 158px; background: var(--card-white); }
  .card-back {
    top: 652px;
    background: radial-gradient(ellipse at 50% 50%, var(--brick-glow) 0%, #b83a20 55%, var(--brick-deep) 100%);
  }

  .brand-block {
    position: absolute;
    left: 470px;
    top: 62px;
    width: 180px;
    text-align: center;
  }
  .brand-name {
    font-family: "Arimo", Arial, sans-serif;
    font-weight: 700;
    color: var(--brick);
    font-size: 27px;
    line-height: 1.05;
    text-transform: uppercase;
    margin: 0;
  }
  .brand-mark {
    display: block;
    width: 14px;
    height: 14px;
    margin: 0 auto 10px;
    background: var(--brick);
  }
  .tagline {
    font-family: "Oswald", "Arial Narrow", sans-serif;
    color: var(--ink-dark);
    margin: 0;
    white-space: nowrap;
  }
  .brand-block .tagline { font-size: 9px; margin-top: 14px; }

  .person {
    position: absolute;
    left: 48px;
    top: 222px;
    font-family: "Arimo", Arial, sans-serif;
  }
  .person-name {
    margin: 0;
    color: var(--brick);
    font-weight: 700;
    font-size: 26px;
    letter-spacing: 0.5px;
    line-height: 1;
  }
  .person-title {
    margin: 6px 0 0;
    color: #6b6b6b;
    font-size: 15px;
  }
  .divider {
    position: absolute;
    left: 48px;
    top: 281px;
    width: 592px;
    height: 1px;
    background: var(--rule);
  }
  .contact-list {
    position: absolute;
    left: 45px;
    top: 290px;
    margin: 0;
    padding: 0;
    list-style: none;
    font-family: "Arimo", Arial, sans-serif;
    font-size: 17px;
    color: var(--ink);
  }
  .contact-list li {
    display: flex;
    align-items: center;
    height: 20.5px;
  }
  .contact-list svg { width: 14px; height: 14px; margin-right: 10px; fill: var(--brick); }
  .address {
    position: absolute;
    right: 44px;
    top: 292px;
    margin: 0;
    text-align: right;
    font-family: "Arimo", Arial, sans-serif;
    font-style: normal;
    font-size: 17px;
    line-height: 20.5px;
    color: var(--ink);
  }
  .band-brick {
    position: absolute;
    left: 0;
    bottom: 0;
    width: 419px;
    height: 16px;
    background: linear-gradient(90deg, var(--brick-deep), #d4471f 45%, var(--brick-deep));
  }
  .band-steel {
    position: absolute;
    left: 422px;
    right: 0;
    bottom: 0;
    height: 16px;
    background: linear-gradient(90deg, var(--steel-dark), var(--steel-light) 45%, var(--steel-dark));
  }

  .back-brand {
    position: absolute;
    left: 0;
    right: 0;
    top: 120px;
    text-align: center;
  }
  .back-brand .brand-name {
    color: #2a1c18;
    font-size: 50px;
  }
  .back-brand .tagline { font-size: 15px; margin-top: 52px; }
</style>
</head>
<body>
<main class="sheet">
  <section class="card card-front" aria-label="Business card front">
    <div class="brand-block">
      <span class="brand-mark"></span>
      <p class="brand-name">Quarlwick<br>Builders</p>
      <p class="tagline">Patios · Sidewalks · Retaining Walls · Foundations</p>
    </div>

    <div class="person">
      <h1 class="person-name">DANA WHITFIELD</h1>
      <p class="person-title">President</p>
    </div>
    <div class="divider"></div>

    <ul class="contact-list">
      <li>
        <svg viewBox="0 0 24 24" aria-hidden="true"><path d="M6.6 10.8c1.4 2.8 3.8 5.1 6.6 6.6l2.2-2.2c.3-.3.7-.4 1-.2 1.1.4 2.3.6 3.6.6.6 0 1 .4 1 1V20c0 .6-.4 1-1 1C10.6 21 3 13.4 3 4c0-.6.4-1 1-1h3.5c.6 0 1 .4 1 1 0 1.2.2 2.4.6 3.6.1.3 0 .7-.2 1z"/></svg>
        555-214-8830
      </li>
      <li>
        <svg viewBox="0 0 24 24" aria-hidden="true"><path d="M7 1h10a2 2 0 0 1 2 2v18a2 2 0 0 1-2 2H7a2 2 0 0 1-2-2V3a2 2 0 0 1 2-2zm0 3v14h10V4zm5 15.5a1.2 1.2 0 1 0 0 2.4 1.2 1.2 0 0 0 0-2.4z"/></svg>
        555-306-1947
      </li>
      <li>
        <svg viewBox="0 0 24 24" aria-hidden="true"><path d="M2 5h20v14H2zm2 2v.4l8 5.2 8-5.2V7zm0 2.8V17h16V9.8l-8 5.2z"/></svg>
        info@quarlwick.com
      </li>
    </ul>

    <address class="address">
      4120 Alder Ridge Road<br>
      Halden, Canada 51820<br>
      www.quarlwick.com
    </address>

    <div class="band-brick"></div>
    <div class="band-steel"></div>
  </section>

  <section class="card card-back" aria-label="Business card back">
    <div class="back-brand">
      <p class="brand-name">Quarlwick Builders</p>
      <p class="tagline">Patios · Sidewalks · Retaining Walls · Foundations</p>
    </div>
  </section>
</main>
</body>
</html>
```